Business Coaching Model and Flow Chart

We need this flowchart, attached, to be updated in a modern and engaging way. This flowchart is the cornerstone of a business coaching class we are running, and will be the main support reference for the people who take the class. We are open to ideas as to how it is presented, but we would like a largely minimalist look that leaves space to be impactful where the key information sites. Our colour scheme is primary red (D51C29), white, grey (333333), black, and secondary green (3C8740). We will also need our logo present (attached).

```html
<!DOCTYPE html>
<html lang="en">
<head>
<meta charset="UTF-8">
<title>Groups to Teams – Through Learning Together</title>
<link href="https://fonts.googleapis.com/css2?family=Montserrat:wght@500;600;700;800;900&display=swap" rel="stylesheet">
<style>
  :root {
    --red: #D51C29;
    --green: #3C8740;
    --grey: #333333;
    --black: #111111;
    --white: #ffffff;
    --paper: #f6f6f6;
    --soft-grey: #d9d9d9;
    --muted: #666666;
  }
  * { margin: 0; padding: 0; box-sizing: border-box; }
  html, body { width: 813px; height: 1200px; overflow: hidden; }
  body { font-family: 'Montserrat', sans-serif; color: var(--grey); background: var(--paper); }
  .canvas { position: relative; width: 813px; height: 1200px; background: var(--paper); overflow: hidden; }

  .brand { position: absolute; left: 0; top: 16px; width: 813px; text-align: center; }
  .brand-dot { width: 96px; height: 96px; border-radius: 50%; background: var(--red); margin: 0 auto; }
  .brand-name { margin-top: 6px; font-size: 12px; font-weight: 800; letter-spacing: .5px; color: var(--red); text-transform: uppercase; }

  .title-band { position: absolute; left: 0; top: 143px; width: 813px; height: 88px; background: var(--red); text-align: center; color: var(--white); }
  .title-band h1 { font-size: 33px; font-weight: 900; line-height: 1; margin-top: 16px; letter-spacing: -.3px; }
  .title-band p { font-size: 19px; font-weight: 800; color: var(--soft-grey); margin-top: 5px; line-height: 1; }
  .foot-band { position: absolute; left: 0; top: 1179px; width: 813px; height: 21px; background: var(--red); }

  .flow-lines { position: absolute; left: 0; top: 0; }

  .icon { position: absolute; border-radius: 6px; background: var(--green); opacity: .85; }

  .step-no { position: absolute; width: 27px; height: 27px; border-radius: 50%; background: var(--black); color: var(--white);
    border: 2px solid var(--white); box-shadow: 0 0 0 1.5px var(--grey); font-size: 14px; font-weight: 800;
    display: flex; align-items: center; justify-content: center; }

  .stage { position: absolute; height: 39px; background: var(--green); color: var(--white); border-radius: 20px;
    display: flex; flex-direction: column; justify-content: center; padding-left: 20px; }
  .stage::before { content: ""; position: absolute; left: -11px; top: 50%; transform: translateY(-50%);
    border-top: 8px solid transparent; border-bottom: 8px solid transparent; border-right: 13px solid var(--green); }
  .stage strong { font-size: 12px; font-weight: 700; line-height: 1.1; letter-spacing: .2px; }
  .stage span { font-size: 11.5px; font-weight: 500; line-height: 1.2; }
  .stage.major { align-items: center; padding-left: 0; }
  .stage.major strong { font-size: 19px; font-weight: 800; }

  .points { position: absolute; list-style: none; }
  .points li { position: relative; padding-left: 12px; font-size: 11px; font-weight: 700; line-height: 13px; color: var(--grey); }
  .points li::before { content: ""; position: absolute; left: 0; top: 3px; width: 7px; height: 7px; border-radius: 50%;
    border: 1.3px solid var(--grey); background: radial-gradient(circle, var(--grey) 45%, transparent 50%); }
  .points.tight li { margin-bottom: 5.6px; }
  .points.wide li { margin-bottom: 6.5px; }
  .points.lead li { font-size: 11.5px; }

  .sub-points { list-style: none; margin: 1px 0 2px 9px; }
  .sub-points li { font-size: 7px; font-weight: 600; line-height: 10.3px; color: var(--muted); padding-left: 8px; margin: 0; }
  .sub-points li::before { width: 3px; height: 3px; top: 3.5px; border: none; background: var(--muted); }
</style>
</head>
<body>
<div class="canvas">

  <header class="brand">
    <div class="brand-dot"></div>
    <div class="brand-name">Mara Vennet</div>
  </header>

  <section class="title-band">
    <h1>GROUPS TO TEAMS</h1>
    <p>THROUGH LEARNING TOGETHER</p>
  </section>

  <svg class="flow-lines" width="813" height="1200" viewBox="0 0 813 1200" aria-hidden="true">
    <g fill="none" stroke="#3C8740" stroke-width="4" stroke-linecap="round" stroke-dasharray="0 8.5">
      <path d="M314 299 H448"/>
      <path d="M748 296 Q780 296 780 312 V470 Q780 486 764 486 H52 Q38 486 38 500 V540 Q38 552 52 552 H100"/>
      <path d="M412 552 H472"/>
      <path d="M732 552 Q780 552 780 568 V700 Q780 713 766 713 H52 Q38 713 38 727 V766 Q38 778 52 778 H100"/>
      <path d="M393 778 H466"/>
      <path d="M766 778 Q780 778 780 794 V1016 Q780 1030 766 1030 H52 Q38 1030 38 1044 V1086 Q38 1098 52 1098 H100"/>
    </g>
    <g fill="#3C8740">
      <path d="M446 293 L457 299 L446 305 Z"/>
      <path d="M772 396 L788 396 L780 414 Z"/>
      <path d="M372 478 L354 486 L372 494 Z"/>
      <path d="M98 545 L110 552 L98 559 Z"/>
      <path d="M772 622 L788 622 L780 640 Z"/>
      <path d="M380 705 L362 713 L380 721 Z"/>
      <path d="M98 771 L110 778 L98 785 Z"/>
      <path d="M446 1022 L428 1030 L446 1038 Z"/>
      <path d="M98 1091 L110 1098 L98 1105 Z"/>
    </g>
  </svg>

  <!-- Step 1 -->
  <div class="icon" style="left:56px;top:281px;width:44px;height:36px" role="img" aria-label="Icon: hand holding a maze"></div>
  <div class="step-no" style="left:107px;top:285px">1</div>
  <div class="stage major" style="left:156px;top:279px;width:155px"><strong>PROBLEM</strong></div>
  <ul class="points tight lead" style="left:151px;top:336px">
    <li>Under-billing</li>
    <li>Staff Retention</li>
    <li>Hard To Recruit</li>
    <li>Client Complaints</li>
    <li>Staff Stress and<br>Burnout</li>
  </ul>
  <ul class="points tight lead" style="left:279px;top:336px">
    <li>Conflict</li>
    <li>Sector Constant<br>Change</li>
    <li>Limited In Best<br>Practice</li>
  </ul>

  <!-- Step 2 -->
  <div class="icon" style="left:466px;top:272px;width:46px;height:45px" role="img" aria-label="Icon: analyst with question mark and bar chart"></div>
  <div class="step-no" style="left:522px;top:285px">2</div>
  <div class="stage" style="left:567px;top:279px;width:177px"><strong>CLARIFY CHALLENGES</strong><span>(Diagnostics)</span></div>
  <ul class="points lead" style="left:595px;top:324px">
    <li style="margin-bottom:5.8px">Scoping</li>
    <li style="margin-bottom:5.8px">Interviews</li>
    <li style="margin-bottom:5.8px">Group Reflection</li>
    <li style="margin-bottom:5.8px">Opinion Surveys</li>
    <li>Certified Assessments
      <ul class="sub-points">
        <li>Personality Styles</li>
        <li>Work Preference</li>
        <li>Strengths &amp; Values</li>
        <li>Trust</li>
        <li>360</li>
      </ul>
    </li>
  </ul>

  <!-- Step 3 -->
  <div class="icon" style="left:118px;top:534px;width:35px;height:35px" role="img" aria-label="Icon: strategy board on easel"></div>
  <div class="step-no" style="left:166px;top:540px">3</div>
  <div class="stage" style="left:214px;top:533px;width:190px"><strong>PLANNING FOR SUCCESS</strong><span>(Make a Plan)</span></div>
  <ul class="points wide lead" style="left:223px;top:596px">
    <li>Team Data Analysis Workshop</li>
    <li>Individual Development Plan</li>
    <li>Team Development Plan</li>
    <li>Organizational Plan</li>
  </ul>

  <!-- Step 4 -->
  <div class="icon" style="left:480px;top:534px;width:36px;height:35px" role="img" aria-label="Icon: gear and wrench"></div>
  <div class="step-no" style="left:523px;top:539px">4</div>
  <div class="stage" style="left:569px;top:533px;width:157px"><strong>LEARN THE TOOLS</strong><span>(Workshops)</span></div>
  <ul class="points lead" style="left:578px;top:584px">
    <li style="color:var(--black)">Foundation Workshops
      <ul class="sub-points">
        <li>Difficult Conversations</li>
        <li>Giving &amp; Receiving Feedback</li>
        <li>Values Alignment</li>
        <li>Shared Purpose</li>
        <li>Ways Of Working</li>
        <li>Diversity</li>
        <li>Well-being</li>
        <li>Time Management</li>
      </ul>
    </li>
    <li style="color:var(--black);margin-top:3px">Customized Workshops</li>
  </ul>

  <!-- Step 5 -->
  <div class="icon" style="left:118px;top:761px;width:35px;height:35px" role="img" aria-label="Icon: person working at laptop"></div>
  <div class="step-no" style="left:166px;top:765px">5</div>
  <div class="stage" style="left:214px;top:759px;width:171px"><strong>DOING</strong><span>(Mastering the Tools)</span></div>
  <ul class="points wide lead" style="left:218px;top:818px">
    <li>Group Coaching</li>
    <li>Team Coaching</li>
    <li>Individual Coaching</li>
    <li>Peer Learning</li>
    <li>Lunch ‘N Learn</li>
  </ul>

  <!-- Step 6 -->
  <div class="icon" style="left:474px;top:760px;width:39px;height:36px;border-radius:50%" role="img" aria-label="Icon: three stars in a cycle"></div>
  <div class="step-no" style="left:523px;top:764px">6</div>
  <div class="stage" style="left:568px;top:759px;width:194px"><strong style="font-size:12px">REFLECT-ADAPT-EMBED</strong></div>
  <ul class="points wide lead" style="left:581px;top:808px">
    <li>Culture Committee</li>
    <li>Embedding Workshop</li>
    <li>Culture Collateral</li>
    <li>WOW Manifesto</li>
    <li>Leadership Team Coaching</li>
    <li>Measure ROI</li>
    <li>Review Success</li>
    <li>Evaluation Surveys</li>
    <li>Temperature Checks</li>
    <li>Recruit To Suit</li>
    <li>Future Proofing - What Next?</li>
  </ul>

  <!-- Step 7 -->
  <div class="icon" style="left:120px;top:1080px;width:33px;height:37px;border-radius:50%" role="img" aria-label="Icon: light bulb with puzzle pieces"></div>
  <div class="step-no" style="left:166px;top:1087px">7</div>
  <div class="stage major" style="left:216px;top:1080px;width:155px"><strong>SOLUTION</strong></div>
  <ul class="points wide lead" style="left:388px;top:1081px">
    <li>Self Awareness &amp;<br>Ownership</li>
    <li>Partnership</li>
    <li>Great Place To Work</li>
    <li>Growth Mindset</li>
  </ul>
  <ul class="points wide lead" style="left:571px;top:1081px">
    <li>Coach Approaching Culture</li>
    <li>Feedback Culture</li>
    <li>Way To Manage Conflict</li>
    <li>Best Practice<br>Communication Skills</li>
  </ul>

  <div class="foot-band"></div>
</div>
</body>
</html>
```